Geschäftspapiere für PARVENTO
Zielgruppe
We sell Tee Times online and in real time for golfers
Aufgabenstellung
We need a layout for a voucher, invoice, letterhead.
Especially the voucher should be easily be printable from any customer at home.
The attached voucher is just an example of which informations need to included

```html
<!DOCTYPE html>
<html lang="de">
<head>
<meta charset="utf-8">
<title>PARVENTO Geschäftspapiere</title>
<link href="https://fonts.googleapis.com/css2?family=Comfortaa:wght@600;700&family=Source+Sans+3:wght@400;600&display=swap" rel="stylesheet">
<style>
  :root{
    --bg:#e6e6e6;
    --paper:#ffffff;
    --green:#8ab220;
    --green-band:#86ad1e;
    --ink:#3c3c3c;
    --ink-soft:#555555;
    --rule:#c9dc8e;
  }
  html,body{margin:0;padding:0;overflow:hidden;}
  body{width:1200px;height:1200px;background:var(--bg);position:relative;
       font-family:"Source Sans 3",Arial,sans-serif;color:var(--ink);}
  .sheet{position:absolute;background:var(--paper);box-shadow:-6px 6px 10px rgba(0,0,0,.18);overflow:hidden;}
  .abs{position:absolute;margin:0;}

  /* vouchers */
  .voucher{left:57px;width:537px;height:268px;}
  .voucher--front{top:369px;}
  .voucher--back{top:675px;}
  .voucher__photo{position:absolute;inset:0;
    background:linear-gradient(160deg,#f6eaa8 0%,#c9c35a 22%,#7f9a2c 45%,#56761d 70%,#3e5a16 100%);}
  .voucher__title{left:29px;top:37px;font-family:"Comfortaa",sans-serif;font-weight:700;
    color:var(--green);font-size:31px;line-height:30px;letter-spacing:.5px;}
  .voucher__title span{display:block;}
  .voucher__title span+span{padding-left:26px;}
  .voucher__band{left:0;top:146px;width:191px;height:39px;background:var(--green-band);}
  .voucher__band p{margin:0;position:absolute;left:54px;top:2px;color:#fff;font-size:13.5px;line-height:18px;}
  .voucher__when{left:54px;top:108px;font-size:13.5px;line-height:18px;color:var(--ink-soft);}
  .course{left:206px;top:107px;font-size:10px;line-height:12.6px;color:var(--ink-soft);}
  .course__name{color:var(--green);font-size:14px;line-height:18px;margin-bottom:1px;display:block;}
  .guests{left:363px;top:127px;font-size:10px;line-height:12.6px;color:var(--ink-soft);}
  .gap{display:block;height:5px;}
  .voucher__foot{left:54px;top:235px;width:465px;font-size:5.6px;line-height:8px;color:var(--ink-soft);}
  .voucher__no{position:absolute;right:0;top:0;color:var(--green);}

  /* letterhead */
  .letter{left:634px;top:221px;width:510px;height:722px;font-size:7.4px;line-height:13px;}
  .brand{left:0;width:100%;top:66px;text-align:center;font-size:31px;font-weight:600;
    letter-spacing:3px;color:var(--green);line-height:36px;}
  .brand__dot{display:block;width:22px;height:22px;border-radius:50%;background:var(--green);margin:0 auto 8px;}
  .sender{left:64px;top:128px;font-size:5.5px;color:var(--ink-soft);}
  .sender b{color:var(--green);font-weight:600;}
  .recipient{left:64px;top:156px;}
  .subject{left:64px;top:262px;font-size:9px;}
  .body{left:64px;top:308px;width:290px;}
  .body p{margin:0 0 13px;}
  .letter__rule{left:64px;top:680px;width:396px;height:1px;background:var(--rule);}
  .letter__foot{left:64px;top:685px;width:396px;font-size:5.6px;line-height:8px;color:var(--ink-soft);text-align:center;}
</style>
</head>
<body>

<section class="sheet voucher voucher--front">
  <div class="voucher__photo" role="img" aria-label="Sunlit golf fairway with golfers walking toward trees"></div>
  <h1 class="abs voucher__title"><span>green fee</span><span>voucher</span></h1>
  <div class="abs voucher__band">
    <p>Date of play 09.02.17<br>Time of play 07:15 am</p>
  </div>
</section>

<section class="sheet voucher voucher--back">
  <h1 class="abs voucher__title"><span>green fee</span><span>voucher</span></h1>
  <p class="abs voucher__when">Date of play 09.02.17<br>Time of play 07:15 am</p>
  <p class="abs course">
    <span class="course__name">Camp Verd</span>
    Ma 13 - Inca - Alcúdia, Km 8,2<br>07300 Inca<span class="gap"></span>
    Phone: 0034 971 552 310/-12<br>Fax: 0034 971 552 319<br>E-Mail: info(at)camp-verd.com<br>GPS Koordinaten
  </p>
  <p class="abs guests">
    Frau Berta Mustermann<br>Herr Max mustermann<span class="gap"></span>
    Kind 1 Mustermann<br>Kind 2 Mustermann<span class="gap"></span><span class="gap"></span><br>Germany
  </p>
  <div class="abs voucher__foot">
    <span class="voucher__no">Voucher N° 17-543</span>
    PARVENTO GbR · Lindenweg 14 · 83607 Holzkirchen · www.parvento.com · bookings@parvento.com · Phone +49 8024 61 57 210<br>
    Please note that the voucher is only valid on the date, time, Golf Course and person mentioned above. Please present this voucher to reception for check-in
  </div>
</section>

<section class="sheet letter">
  <div class="abs brand"><span class="brand__dot"></span>PARVENTO</div>
  <p class="abs sender"><b>PARVENTO GbR</b> · Lindenweg 14 · 83607 Holzkirchen</p>
  <p class="abs recipient">Musterfirma GmbH<br>Herr Mustermann<br>Eine andere Straße 12<br>51249 Köln</p>
  <p class="abs subject">GREEN FEE VOUCHER</p>
  <div class="abs body">
    <p>Sehr geehrter Herr Mustermann,</p>
    <p>jeder Setzer hat für diesen Zweck immer etwas Blindtext parat. Blindtext ist im Umfang von einigen tausend Anschlägen, der für die »äußerliche« Gestaltung einer Publikation verwendet und dessen Inhalt unwichtig ist. Man setzt ihn oft zum Beispiel in verschiedenen Schriften und Schriftgrößen, um anderen zu zeigen, wie eine bestimmte Schrift wirkt. Oder man montiert auch komplette ganze Seiten mit sinnlosen Streifen von Blindtext, um das spätere Aussehen der Seiten zu simulieren.</p>
    <p>Blindtext wird allerdings oft nur für die Teile einer Seite verwendet, die in so kleiner Schrift gesetzt werden, dass sie beim »Überfliegen« ungelesen bleiben. Jeder Setzer hat für diesen Zweck immer etwas Blindtext parat. Blindtext ist Umfang von einigen tausend Anschlägen, der für die »äußerliche« Gestaltung einer Publikation verwendet und dessen Inhalt unwichtig ist.</p>
    <p style="margin-top:20px">Mit freundlichen Grüßen</p>
  </div>
  <div class="abs letter__rule"></div>
  <div class="abs letter__foot">
    PARVENTO GbR · Lindenweg 14 · 83607 Holzkirchen · www.parvento.com · bookings@parvento.com · Phone +49 8024 61 57 210<br>
    Please note that the voucher is only valid on the date, time, Golf Course and person mentioned above. Please present this voucher to reception for check-in
  </div>
</section>

</body>
</html>
```